Business Card Design Project

We consult with hotels on setting rates and maximizing a revenue strategy

Industry/Entity Type

Business

Contact Information for Business Card

I am not sure what I want. Our company offers high level consulting to hotels around the country but we are also laid back. I would like something that is professional but also shows the laid back side

```html
<!DOCTYPE html>
<html lang="en">
<head>
<meta charset="utf-8">
<title>Harborline – Business Card</title>
<link href="https://fonts.googleapis.com/css2?family=Signika:wght@400;600&display=swap" rel="stylesheet">
<style>
  :root{
    --stage:#6c778a;
    --card-top:#c6d6d6;
    --card-bottom:#ffffff;
    --teal:#16706a;
    --teal-soft:#4f9f98;
    --teal-pale:#9fcac4;
    --ink:#2e2622;
    --grey:#555a5c;
  }
  *{margin:0;padding:0;box-sizing:border-box}
  html,body{width:1200px;height:1200px;overflow:hidden}
  body{
    background:var(--stage);
    font-family:"Signika",sans-serif;
    display:flex;align-items:center;justify-content:center;
  }
  .card{
    position:relative;
    width:1040px;height:594px;
    background:linear-gradient(180deg,var(--card-top) 0%,#e4eded 45%,var(--card-bottom) 75%);
    overflow:hidden;
  }
  .card__strip{
    position:absolute;left:0;top:0;width:62px;height:100%;
    background:linear-gradient(180deg,var(--teal-soft) 0%,var(--teal-pale) 60%,#ffffff 100%);
  }
  .card__illustration{
    position:absolute;left:62px;top:0;width:240px;height:100%;
    background:linear-gradient(180deg,#dfeceb 0%,var(--teal-soft) 55%,#cfe3e0 100%);
  }
  .person{position:absolute;left:330px;top:70px}
  .person__name{
    color:var(--teal);font-weight:600;font-size:44px;letter-spacing:1px;line-height:1;
  }
  .person__role{color:var(--grey);font-size:25px;margin-top:14px}
  .contact{
    position:absolute;right:80px;top:150px;
    list-style:none;text-align:right;
    color:var(--grey);font-size:25px;letter-spacing:1px;line-height:38px;
  }
  .contact__item{display:flex;justify-content:flex-end;align-items:center;gap:12px}
  .contact__icon{
    width:26px;height:26px;border:2px solid var(--teal);border-radius:50%;
    color:var(--teal);font-size:14px;line-height:22px;text-align:center;letter-spacing:0;
  }
  .contact__item--plain{padding-right:38px}
  .brand{position:absolute;right:70px;top:330px;text-align:right}
  .brand__name{
    color:var(--ink);font-weight:600;font-size:96px;letter-spacing:2px;line-height:1;
  }
  .brand__tagline{
    color:var(--ink);font-size:34px;margin-top:10px;letter-spacing:.5px;
  }
  .brand__place{
    color:var(--grey);font-size:25px;letter-spacing:3px;margin-top:18px;
  }
</style>
</head>
<body>
  <article class="card">
    <div class="card__strip"></div>
    <div class="card__illustration" role="img" aria-label="Illustration of a teal gothic bridge tower with dark spires"></div>

    <header class="person">
      <h1 class="person__name">ALEX MORENO</h1>
      <p class="person__role">Director</p>
    </header>

    <ul class="contact">
      <li class="contact__item">+63 917 5550142 <span class="contact__icon">T</span></li>
      <li class="contact__item">www.HarborlineRMS.com <span class="contact__icon">W</span></li>
      <li class="contact__item">alex@HarborlineRMS.com <span class="contact__icon">E</span></li>
    </ul>

    <div class="brand">
      <p class="brand__name">HARBORLINE</p>
      <p class="brand__tagline">Revenue Management Solutions</p>
      <p class="brand__place">Dummy City, Dummy Country Land</p>
    </div>
  </article>
</body>
</html>
```